New business card design to go with our new logo

just want an eye-catching business card to go with our new logo. We are open to double sided or single sided. Just want it to have the following info on it. Whatever layout you think looks best.

First and Last Name
Title
Phone 801-555-0187
Address 312 W. Larkmoor Avenue Orem UT 84057
Email thecrew@meadowstailandkennel.example

Industry/Entity Type

Business

```html
<!DOCTYPE html>
<html lang="en">
<head>
<meta charset="utf-8">
<title>Meadow's Tail &amp; Kennel – Business Card</title>
<link rel="stylesheet" href="https://fonts.googleapis.com/css2?family=Lato:wght@400;700&display=swap">
<style>
  :root {
    --bg: #ecebe8;
    --card: #ffffff;
    --sky: #2ea6da;
    --sky-deep: #2596c9;
    --tangerine: #f08a3c;
    --ink: #2b2b2b;
    --white: #ffffff;
  }
  * { box-sizing: border-box; margin: 0; padding: 0; }
  html, body {
    width: 1200px; height: 900px; overflow: hidden;
    background: var(--bg);
    font-family: "Lato", Arial, sans-serif;
  }
  .business-card {
    position: absolute; left: 120px; top: 154px;
    width: 960px; height: 592px;
    background: var(--card);
    overflow: hidden;
    box-shadow: 0 6px 24px rgba(0,0,0,0.12);
  }
  .dog-artwork {
    position: absolute; left: 485px; top: 0;
    width: 475px; height: 592px;
    background: linear-gradient(160deg, var(--sky) 0%, var(--sky-deep) 100%);
  }
  .brand {
    position: absolute; left: 44px; top: 60px;
    width: 300px;
    display: flex; flex-direction: column; align-items: center; gap: 22px;
  }
  .brand-dot {
    width: 150px; height: 150px; border-radius: 50%;
    border: 7px solid var(--tangerine);
  }
  .brand-name {
    color: var(--tangerine);
    font-weight: 700; font-size: 34px; line-height: 1.1;
    text-align: center;
  }
  .person {
    position: absolute; left: 46px; top: 356px;
  }
  .person-name {
    font-size: 31px; font-weight: 700;
    font-variant: small-caps; letter-spacing: 0.5px;
  }
  .person-name .first { color: var(--tangerine); }
  .person-name .last { color: var(--sky); }
  .person-title {
    font-size: 23px; color: var(--ink); margin-top: 2px;
  }
  .contact-list {
    position: absolute; left: 42px; top: 455px;
    list-style: none;
    font-size: 21px; color: var(--ink);
  }
  .contact-list li {
    display: flex; align-items: center; gap: 6px;
    height: 32px;
  }
  .contact-list svg { width: 16px; height: 16px; flex: none; }
  .address {
    position: absolute; right: 42px; top: 320px;
    text-align: right; color: var(--white);
    font-size: 24px; line-height: 33px;
    font-style: normal;
  }
  .base-stripe {
    position: absolute; left: 0; bottom: 0;
    width: 566px; height: 15px;
    background: var(--sky);
  }
</style>
</head>
<body>
  <div class="business-card">
    <div class="dog-artwork" role="img" aria-label="Large blue and orange illustration of a smiling dog's head and chest"></div>

    <div class="brand">
      <div class="brand-dot"></div>
      <div class="brand-name">Meadow's Tail &amp; Kennel</div>
    </div>

    <div class="person">
      <div class="person-name"><span class="first">Daniel</span> <span class="last">Harper</span></div>
      <div class="person-title">Managing Director</div>
    </div>

    <ul class="contact-list">
      <li>
        <svg viewBox="0 0 16 16"><path fill="#f08a3c" d="M2 5c0-2 2-3 6-3s6 1 6 3v1h-3V5H5v1H2z M4 7h8l1 6H3z"/><circle cx="8" cy="10" r="1.6" fill="#fff"/></svg>
        801-555-0187
      </li>
      <li>
        <svg viewBox="0 0 16 16"><rect x="1" y="3" width="14" height="10" rx="1" fill="#f08a3c"/><path d="M1.5 4l6.5 5 6.5-5" fill="none" stroke="#fff" stroke-width="1.3"/></svg>
        thecrew@meadowstailandkennel.example
      </li>
      <li>
        <svg viewBox="0 0 16 16"><circle cx="8" cy="8" r="7" fill="#f08a3c"/><path d="M1 8h14M8 1c3 3 3 11 0 14M8 1c-3 3-3 11 0 14" fill="none" stroke="#fff" stroke-width="1"/></svg>
        www.meadowstailandkennel.example
      </li>
    </ul>

    <address class="address">
      312 W. Larkmoor Avenue<br>
      Orem<br>
      UT 84057
    </address>

    <div class="base-stripe"></div>
  </div>
</body>
</html>
```